Pantry Barn EPP Mailer

This card will be mailed to local communities to make people aware of the ALL the Products - particularly local food - offered at Pantry Barn of Willowbrook. On the attached copy, the content in BOLD should be emphasized. Not all of the photos need to be utilized, but wanted to provide an assortment that shows off food and merchandise. Please note - this card is 8 in. x 6.5 inches and MUST be laid out to conform the the Each Porch Post format attached - with mailing and postage spaces left in the areas indicated on one side.

```html
<!DOCTYPE html>
<html lang="en">
<head>
<meta charset="utf-8">
<title>Pantry Barn of Willowbrook – Mailer</title>
<link rel="stylesheet" href="https://fonts.googleapis.com/css2?family=Montserrat:wght@800&family=Open+Sans:wght@400;600;700&display=swap">
<style>
  :root {
    --backdrop: #b3b3b3;
    --card: #ffffff;
    --brand-green: #58a345;
    --info-gray: #737373;
    --ink: #333333;
    --white: #ffffff;
  }
  * { box-sizing: border-box; margin: 0; padding: 0; }
  html, body { width: 1200px; height: 1011px; overflow: hidden; background: var(--backdrop); }
  .mailer {
    position: absolute; left: 94.5px; top: 94.5px;
    width: 1010.5px; height: 820.5px; background: var(--card);
  }
  .headline-panel {
    position: absolute; left: 0; top: 0; width: 501px; height: 177.5px;
    background: var(--brand-green);
  }
  .headline {
    position: absolute; left: 29px; top: 62px;
    font-family: "Montserrat", sans-serif; font-weight: 800;
    font-size: 29.5px; line-height: 31px; color: var(--white); letter-spacing: 0.1px;
  }
  .product-gallery {
    position: absolute; left: 5px; top: 183.5px; width: 999px;
    display: grid; grid-template-columns: 160px 160.5px 160px 164.5px 164.5px 161px;
    grid-template-rows: 123px 123.5px; column-gap: 5.2px; row-gap: 5.5px;
  }
  .product-photo { display: block; }
  .features-panel {
    position: absolute; left: 0; top: 441px; width: 165px; height: 168px;
    background: var(--brand-green); padding: 33px 0 0 18px;
    font-family: "Open Sans", sans-serif; font-weight: 600;
    font-size: 18.5px; line-height: 26px; color: var(--white);
  }
  .features-panel li { list-style: none; white-space: nowrap; }
  .intro-copy {
    position: absolute; left: 183.5px; top: 461px; width: 320px;
    font-family: "Open Sans", sans-serif; font-size: 15.6px; line-height: 21.5px; color: var(--ink);
  }
  .intro-copy strong { font-weight: 700; }
  .contact-panel {
    position: absolute; left: 0; top: 614.5px; width: 501px; height: 206px;
    background: var(--info-gray); color: var(--white); text-align: center;
    font-family: "Open Sans", sans-serif;
  }
  .contact-panel h2 {
    margin-top: 26px; font-family: "Montserrat", sans-serif; font-weight: 800;
    font-size: 24.5px; line-height: 30px;
  }
  .contact-panel address { font-style: normal; margin-top: 17px; font-size: 18px; line-height: 26px; }
  .contact-panel .corner { font-weight: 600; }
</style>
</head>
<body>
  <main class="mailer">
    <header class="headline-panel">
      <h1 class="headline">Pantry Barn of Willowbrook<br>proudly features:</h1>
    </header>

    <section class="product-gallery">
      <div class="product-photo" role="img" aria-label="Bagged local flours and fresh bread loaves on shelves" style="background:linear-gradient(#b99a6c,#8a6a45)"></div>
      <div class="product-photo" role="img" aria-label="Display rack of outdoor and mountain themed stickers" style="background:linear-gradient(#c9b48f,#6f7d86)"></div>
      <div class="product-photo" role="img" aria-label="Shelves of sauces, oils and condiments" style="background:linear-gradient(#c9a370,#7a3e2e)"></div>
      <div class="product-photo" role="img" aria-label="Soy sauces, vinegars and jars of sauerkraut" style="background:linear-gradient(#8a5a2c,#c9a046)"></div>
      <div class="product-photo" role="img" aria-label="Basket of local peaches with chalkboard price sign" style="background:linear-gradient(#b7a47c,#c56a3e)"></div>
      <div class="product-photo" role="img" aria-label="Glass deli case with baked goods" style="background:linear-gradient(#c7c2b6,#8d7a5c)"></div>
      <div class="product-photo" role="img" aria-label="Pints of ice cream in a freezer" style="background:linear-gradient(#c25a8a,#d6b79a)"></div>
      <div class="product-photo" role="img" aria-label="Decorative pillows and kitchen towels on display" style="background:linear-gradient(#9ccf8a,#3f86a8)"></div>
      <div class="product-photo" role="img" aria-label="Crate of organic heirloom tomatoes with price sign" style="background:linear-gradient(#d9753a,#b89264)"></div>
      <div class="product-photo" role="img" aria-label="Gluten free products shelf and housewares aisle" style="background:linear-gradient(#c4a57e,#8b7360)"></div>
      <div class="product-photo" role="img" aria-label="Close view of ripe peaches in a basket" style="background:linear-gradient(#d06d3a,#a8452b)"></div>
      <div class="product-photo" role="img" aria-label="Produce stand with berries and fresh vegetables" style="background:linear-gradient(#6d8a7a,#a7583c)"></div>
    </section>

    <ul class="features-panel">
      <li>Open 7 Days!</li>
      <li>Family-Run</li>
      <li>Locally Focused</li>
      <li>Kind Service</li>
    </ul>

    <p class="intro-copy">Discover our many <strong>Regional Food Items</strong>.<br>Choosing locally grown/produced, healthy<br>food benefits you, your neighbors<br>&amp; our planet. We like that.<br>Please stop in and see the changes we<br>have in store...with more to come!</p>

    <footer class="contact-panel">
      <h2>Make A Day of It in Willowbrook!</h2>
      <address>
        <span class="corner">Corner of Elm &amp; Mill Streets</span><br>
        212 Elm Street, Willowbrook<br>
        555 013-2290&nbsp; hello@pantrybarn.net<br>
        Web: PBOW.net
      </address>
    </footer>
  </main>
</body>
</html>
```